Harold Brisk Mechanical business cards

We need business cards designed for "Harold Brisk Mechanical" "Mechanical & Electrical Contractors" "Specializing in Service & Installation"
"Cooling, Heating, Service, Installations, Residential, Commercial"

```html
<!DOCTYPE html>
<html lang="en">
<head>
<meta charset="utf-8">
<title>Harold Brisk Mechanical – Business Cards</title>
<link rel="stylesheet" href="https://fonts.googleapis.com/css2?family=Open+Sans:wght@400;600&family=Work+Sans:wght@400;500&display=swap">
<style>
  :root {
    --bg: #3b3431;
    --card: #141414;
    --red: #e3242b;
    --white: #ffffff;
    --soft: #d9d9d9;
  }
  * { margin: 0; padding: 0; box-sizing: border-box; }
  html, body { width: 1200px; height: 715px; overflow: hidden; background: var(--bg); }
  .canvas { position: relative; width: 1200px; height: 715px; }

  .card {
    position: absolute;
    top: 208px;
    width: 525px;
    height: 300px;
    background: var(--card);
    overflow: hidden;
    box-shadow: 0 10px 24px rgba(0,0,0,.45);
  }
  .card--front { left: 45px; }
  .card--back { left: 630px; }

  .brand {
    display: flex;
    align-items: center;
    gap: 10px;
  }
  .brand__square { width: 26px; height: 26px; background: var(--red); flex: none; }
  .brand__name {
    font-family: "Open Sans", sans-serif;
    font-weight: 600;
    color: var(--white);
    letter-spacing: .5px;
    line-height: 1.05;
    text-transform: uppercase;
  }

  /* Front */
  .card--front .brand { position: absolute; top: 78px; left: 0; right: 0; justify-content: center; }
  .card--front .brand__name { font-size: 24px; }
  .front__info {
    position: absolute; top: 152px; left: 0; right: 0;
    text-align: center;
    font-family: "Open Sans", sans-serif;
    font-size: 13px; line-height: 22px;
    color: var(--white);
  }

  /* Back */
  .person { position: absolute; top: 52px; left: 40px; font-family: "Work Sans", sans-serif; }
  .person__name { color: var(--red); font-size: 22px; font-weight: 500; letter-spacing: .5px; text-transform: uppercase; }
  .person__role { color: var(--white); font-size: 13px; margin-top: 2px; }
  .rule { position: absolute; top: 115px; left: 40px; width: 450px; height: 1px; background: var(--red); }
  .contact { position: absolute; top: 132px; left: 40px; list-style: none; font-family: "Work Sans", sans-serif; font-size: 14px; color: var(--white); }
  .contact li { display: flex; align-items: center; gap: 8px; line-height: 24px; }
  .contact svg { width: 10px; height: 10px; fill: var(--red); }
  .card--back .brand { position: absolute; top: 58px; right: 36px; }
  .card--back .brand__name { font-size: 20px; text-align: right; }
  .address {
    position: absolute; right: 36px; top: 192px; text-align: right;
    font-family: "Work Sans", sans-serif; font-size: 14px; line-height: 21px; color: var(--white);
  }
  .web { position: absolute; right: 36px; top: 246px; font-family: "Work Sans", sans-serif; font-size: 14px; color: var(--white); }
  .band-line { position: absolute; left: 0; top: 232px; width: 300px; height: 3px; background: var(--white); }
  .band { position: absolute; left: 0; top: 240px; width: 300px; height: 60px; background: var(--red); }
  .band-tail { position: absolute; left: 300px; top: 284px; width: 225px; height: 16px; background: var(--red); }
  .tail-line { position: absolute; right: 36px; top: 272px; width: 150px; height: 3px; background: var(--white); }
</style>
</head>
<body>
<main class="canvas">

  <section class="card card--front" aria-label="Card front">
    <div class="brand">
      <span class="brand__square"></span>
      <span class="brand__name">Harold Brisk Mechanical</span>
    </div>
    <div class="front__info">
      <p>Harold Brisk Mechanical</p>
      <p>Mechanical &amp; Electrical Contractors - Specializing in Service &amp; Installation</p>
      <p>Cooling - Heating - Service - Installations - Residential - Commercial</p>
    </div>
  </section>

  <section class="card card--back" aria-label="Card back">
    <div class="person">
      <p class="person__name">Daniel Reyes</p>
      <p class="person__role">Managing Partner</p>
    </div>
    <div class="rule"></div>
    <ul class="contact">
      <li><svg viewBox="0 0 10 10" aria-hidden="true"><path d="M2 0h2l1 3-1.5 1a6 6 0 0 0 2.5 2.5L7 5l3 1v2a2 2 0 0 1-2 2A8 8 0 0 1 0 2a2 2 0 0 1 2-2z"/></svg>555-014-2290</li>
      <li><svg viewBox="0 0 10 10" aria-hidden="true"><path d="M0 2h10v6H0zM1 3v.3l4 2.5 4-2.5V3z"/></svg>info@haroldbrisk.com</li>
    </ul>
    <div class="brand">
      <span class="brand__square"></span>
      <span class="brand__name">Harold Brisk<br>Mechanical</span>
    </div>
    <div class="address">
      <p>1870 Larkfield Road</p>
      <p>Dayton, OH 45402</p>
    </div>
    <p class="web">www.haroldbrisk.com</p>
    <div class="band-line"></div>
    <div class="band"></div>
    <div class="band-tail"></div>
    <div class="tail-line"></div>
  </section>

</main>
</body>
</html>
```